Letterhead Design Project

Attached is our new Logo and a copy of our old letter head
Looking to rebrand with our new logo

Reason: I want to show a business card design

Industry/Entity Type

Film Production

Colors

Requirements
Must have
• The information on the old letterhead

```html
<!DOCTYPE html>
<html lang="en">
<head>
<meta charset="utf-8">
<title>KORA International Letterhead</title>
<link rel="stylesheet" href="https://fonts.googleapis.com/css2?family=Arimo:wght@400;700&display=swap">
<style>
  :root {
    --orange: #f58634;
    --blue: #2e9ad6;
    --ink: #1d1d1b;
    --brand-blue: #1f8fc9;
    --paper: #ffffff;
    --decor-light: #ececec;
    --decor-mid: #d9d9d9;
  }
  html, body {
    margin: 0;
    padding: 0;
    width: 1000px;
    height: 1200px;
    overflow: hidden;
    background: var(--paper);
  }
  .letterhead {
    position: relative;
    width: 1000px;
    height: 1200px;
    background: var(--paper);
    font-family: "Arimo", Arial, sans-serif;
    color: var(--ink);
    overflow: hidden;
  }
  .edge-band {
    position: absolute;
    top: 0;
    left: 0;
    width: 50px;
    height: 1122px;
    background: var(--orange);
  }
  .edge-stripe {
    position: absolute;
    top: 0;
    left: 51px;
    width: 11px;
    height: 1122px;
    background: var(--blue);
  }
  .brand {
    position: absolute;
    top: 84px;
    left: 76px;
    width: 150px;
    display: flex;
    align-items: center;
    gap: 8px;
  }
  .brand-dot {
    flex: none;
    width: 14px;
    height: 14px;
    border-radius: 50%;
    background: var(--orange);
  }
  .brand-name {
    font-weight: 700;
    font-size: 14px;
    letter-spacing: 1px;
    line-height: 20px;
    color: var(--brand-blue);
    white-space: nowrap;
  }
  .contact {
    position: absolute;
    top: 80px;
    left: 230px;
    width: 340px;
    text-align: center;
    font-size: 9.8px;
    font-weight: 700;
    letter-spacing: -0.2px;
    line-height: 12px;
    white-space: nowrap;
  }
  .contact p { margin: 0 0 12px; }
  .contact .tagline { margin-left: 30px; }
  .contact .phone-line { margin-left: 40px; }
  .contact-rule {
    position: absolute;
    top: 150px;
    left: 240px;
    width: 321px;
    height: 2px;
    background: var(--blue);
  }
  .partner-badge {
    position: absolute;
    top: 62px;
    left: 580px;
    width: 144px;
    height: 66px;
  }
  .decor-slate {
    position: absolute;
    top: 540px;
    left: 293px;
    width: 503px;
    height: 582px;
    background: linear-gradient(160deg, var(--decor-light) 0%, var(--decor-mid) 60%, var(--decor-light) 100%);
    clip-path: polygon(100% 0, 100% 100%, 14% 100%, 10% 36%, 60% 12%);
  }
  .divisions {
    position: absolute;
    top: 1020px;
    left: 150px;
    width: 500px;
    text-align: center;
    font-size: 13px;
    line-height: 20px;
    white-space: nowrap;
  }
  .divisions p { margin: 0; }
  .divisions .note { font-size: 11.5px; font-weight: 700; }
  .divisions .note span { font-weight: 400; font-size: 13px; }
</style>
</head>
<body>
  <main class="letterhead">
    <div class="edge-band"></div>
    <div class="edge-stripe"></div>

    <div class="brand">
      <span class="brand-dot"></span>
      <span class="brand-name">KORA<br>INTERNATIONAL</span>
    </div>

    <header class="contact">
      <p class="tagline">Supply &amp; Management of Infrastructure &amp; Logistics</p>
      <p>P.O. Box 482 Eastvale QLD 4390&nbsp;&nbsp;&nbsp;P.O.Box 731 Millbrook NSW 2188</p>
      <p class="phone-line">Ph. 0400 582 617&nbsp;&nbsp;&nbsp;Email. office@kora.com.au</p>
    </header>
    <div class="contact-rule"></div>

    <svg class="partner-badge" viewBox="0 0 144 66" role="img" aria-label="Partner badge">
      <ellipse cx="72" cy="42" rx="70" ry="22" fill="#d9e6f4" stroke="#2e5fa8" stroke-width="2"/>
    </svg>

    <div class="decor-slate" role="img" aria-label="Faint film clapperboard decoration"></div>

    <footer class="divisions">
      <p>&#9830; KORA Film Services&nbsp;&nbsp;&#9830;&nbsp;&nbsp;KORA Pilot Escorts &#9830; KORA Tour Management &#9830;</p>
      <p>&#9830; KORA Driver &#9830;</p>
      <p class="note">are divisions of <span>KORA International Pty Ltd</span></p>
      <p>ACN 408 216 573&nbsp;&nbsp;ABN 52 408 216 573</p>
    </footer>
  </main>
</body>
</html>
```